Graphic design of labels for scented candles

Following a change in our team structure, a deadline was put in place and the brief changed.
We need a beautiful label for our candles, one that sticks *all around the glass*. Must obviously include our logo as well as the description of the perfume.
The clientele is mainly female, between 35 and 65 years old, of a classic nature.
Brand values:
Feminine
Warm-joyful
Sophisticated-elegant
Eco-friendly, pet-friendly
Natural
Inspires confidence.
The idea is to have something different, the final appearance must be elegant and refined, which will be your challenge given the shape.

What we need:
- changeable colors
- small transparent elements which can be printed on a gold or silver paper background (example: logo, frame, elements, etc.)

- the logo (black or very dark gray) must be present + text "vegetable candle", then the perfume and below:
vegetable wax - handcrafted"
I am attaching a picture of our current labels to the files.
For the size I'll let you manage.
These labels can also be assigned to derived products such as room fragrances, pillow mists, etc.
The brand targets the middle class and above.
For the fonts I leave the choice to you.
Thank you and good luck to all !

Update: there is no longer a cat's head as a background shape, you have free choice.
THANKS

Target Market(s)

Women aged 35 to 65

Industry/Entity Type

Industrie du Parfum

Colors
00AB8E
00BBA5
67D7C9
C6EFE9
E9F9F6
59FF00
82FF00
B8FF75
E3FFCB
F4FFEA
FFF300
FFF600
FEFA6F
FFFEC7
FFFEE8
FFC000
F8CF3A
FAE287
FDF2CF
FEFAEE
F0912C
F2A743
F7CA91
FBE8D2
FDF5EE
EE7325
F08F49
F5BC92
FAE3D3
FDF4ED
EB3D1F
EC4F4E
F09395
F8D3D4
FCEDEE
E54698
E96AAD
F1A4CE
F9D9EA
FCEFF6
A7469A
B969AE
D3A5CF
EDDBEB
F8F0F9
6B429C
8869AF
B7A5CE
E3DAEB
F3F0F8

Requirements
Must have
• modifiable colors - small transparent elements which can be printed on a gold or silver paper background (example: frame, elements, etc.) - the logo (black or very dark gray) must be present + text "vegetable candle, then the perfume and below: vegetable wax - handcrafted"
Nice to have
• Elements that could be made transparent (logo text frame) to be able to edit on gold papers and give a luxurious appearance
Should not have
• no childish appearance.

```html
<!DOCTYPE html>
<html lang="en">
<head>
<meta charset="utf-8">
<title>Lunelle Vegetable Candle Label</title>
<link href="https://fonts.googleapis.com/css2?family=Montserrat:wght@500;600&family=Playball&display=swap" rel="stylesheet">
<style>
  :root {
    --page-bg: #f3efe9;
    --label-paper: #f7f5f1;
    --gold: #c8995c;
    --gold-light: #e4c79a;
    --badge-fill: #0c0c0c;
    --badge-edge: #00ab8e;
    --accent-green: #00ab8e;
    --text-light: #e9e6e1;
    --flag-red: #e2231a;
  }
  html, body {
    margin: 0;
    width: 1200px;
    height: 1200px;
    overflow: hidden;
    background: var(--page-bg);
  }
  .label-wrap {
    position: absolute;
    left: 0;
    top: 300px;
    width: 1200px;
    height: 600px;
    background: var(--label-paper);
  }
  .gold-band {
    position: absolute;
    left: 0;
    width: 100%;
    background: linear-gradient(180deg, var(--gold-light), var(--gold) 50%, var(--gold-light));
  }
  .gold-band--upper { top: 170px; height: 14px; }
  .gold-band--upper-thin { top: 192px; height: 4px; }
  .gold-band--lower { top: 500px; height: 16px; }
  .badge {
    position: absolute;
    left: 320px;
    top: 60px;
    width: 560px;
    height: 420px;
  }
  .badge svg { position: absolute; inset: 0; }
  .badge-content {
    position: absolute;
    inset: 0;
    display: flex;
    flex-direction: column;
    align-items: center;
    font-family: "Montserrat", sans-serif;
  }
  .brand-name {
    margin-top: 92px;
    font-weight: 600;
    font-size: 46px;
    letter-spacing: 2px;
    color: var(--gold);
    display: flex;
    align-items: center;
    gap: 12px;
  }
  .brand-dot {
    width: 14px; height: 14px;
    border-radius: 50%;
    background: var(--gold);
  }
  .rule {
    width: 320px;
    height: 2px;
    background: var(--gold);
    margin-top: 8px;
  }
  .product-type {
    margin-top: 8px;
    font-weight: 500;
    font-size: 26px;
    letter-spacing: 1px;
    color: var(--text-light);
  }
  .scent-name {
    margin-top: 10px;
    font-family: "Playball", cursive;
    font-size: 78px;
    line-height: 1;
    color: var(--accent-green);
  }
  .claims {
    margin-top: 26px;
    display: flex;
    align-items: center;
    gap: 10px;
    font-weight: 500;
    font-size: 15px;
    color: var(--text-light);
  }
  .claim-icon {
    width: 12px; height: 12px;
    border: 1.5px solid var(--gold);
    border-radius: 50%;
  }
  .rule--short { width: 300px; height: 1px; margin-top: 4px; }
  .site {
    margin-top: 4px;
    font-size: 14px;
    color: var(--text-light);
  }
  .origin-flag {
    margin-top: 8px;
    width: 18px; height: 18px;
    background: var(--flag-red);
    position: relative;
  }
  .origin-flag::before, .origin-flag::after {
    content: "";
    position: absolute;
    background: #fff;
  }
  .origin-flag::before { left: 7px; top: 3px; width: 4px; height: 12px; }
  .origin-flag::after { left: 3px; top: 7px; width: 12px; height: 4px; }
</style>
</head>
<body>
  <div class="label-wrap">
    <div class="gold-band gold-band--upper"></div>
    <div class="gold-band gold-band--upper-thin"></div>
    <div class="gold-band gold-band--lower"></div>

    <div class="badge">
      <svg viewBox="0 0 560 420" width="560" height="420" aria-hidden="true">
        <path d="M40 70 Q280 20 520 70 L520 230 Q500 360 280 410 Q60 360 40 230 Z"
              fill="var(--badge-fill)" stroke="var(--badge-edge)" stroke-width="5" stroke-linejoin="round"/>
      </svg>
      <div class="badge-content">
        <div class="brand-name"><span class="brand-dot"></span>Lunelle</div>
        <div class="rule"></div>
        <div class="product-type">VEGETABLE CANDLE</div>
        <div class="scent-name">Perfume</div>
        <div class="claims"><span class="claim-icon"></span>VEGETABLE WAX - HANDCRAFTED<span class="claim-icon"></span></div>
        <div class="rule rule--short"></div>
        <div class="site">lunelle-candle.com</div>
        <div class="origin-flag"></div>
      </div>
    </div>
  </div>
</body>
</html>
```